Wine Label for a White and a Red Wine from Italy

We have a very good idea of what we want with artwork. We need you to please design a 'template' with the text so we can change out the artwork from year to year. Samples are shown of what we are looking for. We are looking for options with the two basic designs. Brand name of wine is: Valora del Torrino. Both wines are in a light green Bordeaux-style bottle (note: we don't show a light green bottle in the mockup but please remember the bottle is light green). Artwork is provided. We'd like to see either the green or blue butterfly on the white wine, the red butterfly is for the red wine. Please base the design on the attached label from Ashby and/or the attached label from Chateau Vellanges.

Target Market(s)

Millennials, women

Requirements
Must have
• The artwork (butterflies) attached.
Nice to have
• Elegant, readable fonts. Please make the text so it can be changed by the printer. Please make it so the artwork can be changed too.

```html
<!DOCTYPE html>
<html lang="en">
<head>
<meta charset="utf-8">
<title>Valora del Torrino – Rosso Labels</title>
<link href="https://fonts.googleapis.com/css2?family=Tenor+Sans&family=Crimson+Pro:wght@400&display=swap" rel="stylesheet">
<style>
  :root {
    --backdrop: #d9d9d9;
    --label-paper: #fdfdfc;
    --ink-brand: #4a4a4a;
    --ink-text: #2f2f2f;
    --art-light: #f3cb4a;
    --art-deep: #e3a81e;
  }
  * { margin: 0; padding: 0; box-sizing: border-box; }
  html, body {
    width: 1200px;
    height: 1009px;
    overflow: hidden;
    background: var(--backdrop);
  }
  .canvas {
    position: relative;
    width: 1200px;
    height: 1009px;
    display: flex;
    justify-content: space-evenly;
    align-items: center;
  }
  .label {
    position: relative;
    width: 502px;
    height: 820px;
    background: var(--label-paper);
    box-shadow: 0 2px 10px rgba(0,0,0,0.12);
    text-align: center;
    color: var(--ink-text);
  }
  .label > * {
    position: absolute;
    left: 0;
    right: 0;
  }
  .brand-name {
    top: 64px;
    font-family: "Tenor Sans", sans-serif;
    font-size: 64px;
    font-weight: 400;
    color: var(--ink-brand);
    line-height: 1;
  }
  .brand-sub {
    top: 130px;
    font-family: "Tenor Sans", sans-serif;
    font-size: 26px;
    color: var(--ink-brand);
    line-height: 1;
  }
  .artwork {
    top: 185px;
    left: 91px;
    right: auto;
    width: 320px;
    height: 320px;
    background: linear-gradient(160deg, var(--art-light), var(--art-deep));
  }
  .selection {
    top: 540px;
    font-family: "Crimson Pro", serif;
    font-size: 25px;
    letter-spacing: 0.5px;
  }
  .vintage {
    top: 590px;
    font-family: "Crimson Pro", serif;
    font-size: 22px;
  }
  .wine-type {
    top: 625px;
    font-family: "Crimson Pro", serif;
    font-size: 37px;
    line-height: 1;
  }
  .region {
    top: 659px;
    font-family: "Crimson Pro", serif;
    font-size: 24px;
    line-height: 1;
  }
  .producer {
    top: 706px;
    font-family: "Crimson Pro", serif;
    font-size: 18px;
  }
  .farming {
    top: 753px;
    font-family: "Crimson Pro", serif;
    font-size: 17px;
  }
</style>
</head>
<body>
  <main class="canvas">
    <section class="label label--rosso-a">
      <h1 class="brand-name">Valora</h1>
      <p class="brand-sub">del Torrino</p>
      <div class="artwork" role="img" aria-label="Artwork placeholder: red butterfly painting on yellow brush strokes (round version)"></div>
      <p class="selection">BARREL SELECT</p>
      <p class="vintage">2018</p>
      <p class="wine-type">Rosso</p>
      <p class="region">Piemonte, Italy</p>
      <p class="producer">Artisanally Crafted by Cantina Quattro Venti</p>
      <p class="farming">sustainably farmed</p>
    </section>
    <section class="label label--rosso-b">
      <h1 class="brand-name">Valora</h1>
      <p class="brand-sub">del Torrino</p>
      <div class="artwork" role="img" aria-label="Artwork placeholder: red butterfly painting on yellow palette-knife strokes"></div>
      <p class="selection">BARREL SELECT</p>
      <p class="vintage">2018</p>
      <p class="wine-type">Rosso</p>
      <p class="region">Piemonte, Italy</p>
      <p class="producer">Artisanally Crafted by Cantina Quattro Venti</p>
      <p class="farming">sustainably farmed</p>
    </section>
  </main>
</body>
</html>
```